Dental Patient Education Single page-Multiple pages needed.

I am creating a unique dental patient education materials for resale. I work in the dental industry, training dentists and thier teams how to improve patient acceptance rates for treatment. I see a need that all patient education material is designed incorrectly. I want to fix this by creating patient education material that educated patients based on all of the treatment options for a diagnosed condition. Tradidional patient education material reads like a catalog of procedures. This format is not effective for helping the patient quickly understand the consequences of non treatment and the benefits and disadvantages of their treatment options. Specifics of the Job:The design images must be royalty free.I will provide the text.Initially there are for major diagnosed conditions: Infected Tooth Treatment Options, Single to Multiple Missing tooth Treatment Options, Full Arch of Missing Teeth Treatment Options, and Full Arch Fixed Dental Implant Treatment OptionsThe layout should mirror the attached sample of Single Missing Tooth Treatment Options.This is a project that will require edits and redesigned based on testing.I also need this in Adobe, so it can be customized/branded for a dental office.

Target Market(s)

Dental office professionals to educate patients.

Font styles to use
Sans Serif

Colors
3277b5

Requirements
Must have
• Professional look and feel
• Royalty free images
• Easy to read

```html
<!DOCTYPE html>
<html lang="en">
<head>
<meta charset="UTF-8">
<title>Single Missing Tooth – Your Options for Treatment</title>
<link href="https://fonts.googleapis.com/css2?family=Raleway:wght@400;500;600;700;800&display=swap" rel="stylesheet">
<style>
  :root{
    --navy:#13285a;
    --blue:#3277b5;
    --bright:#1c7fd0;
    --ink:#2b2f3a;
    --paper:#ffffff;
    --page-bg:#e9ecf1;
    --gum:#d98a93;
  }
  *{box-sizing:border-box;margin:0;padding:0}
  html,body{width:1200px;height:870px;overflow:hidden;background:var(--page-bg);font-family:"Raleway",sans-serif;color:var(--ink)}
  .flyer{position:absolute;left:300px;top:20px;width:600px;height:830px;background:var(--paper);overflow:hidden;box-shadow:0 6px 24px rgba(0,0,0,.15)}
  .header-shape{position:absolute;left:0;top:0;width:600px;height:300px}
  .title{position:absolute;left:0;right:0;top:28px;text-align:center;color:#fff;font-weight:800;font-size:40px;letter-spacing:.5px;text-transform:uppercase}
  .subtitle-band{position:absolute;left:70px;right:70px;top:84px;height:46px;background:var(--blue);color:#fff;font-weight:600;font-size:30px;text-align:center;line-height:46px}
  .intro{position:absolute;left:80px;right:80px;top:142px;text-align:center;color:#fff;font-size:12px;line-height:1.4}
  .pitch{position:absolute;left:60px;right:60px;top:184px;text-align:center;color:#fff;font-weight:700;font-size:18px;line-height:1.3}
  .option-tag{position:absolute;background:var(--navy);color:#fff;font-weight:700;font-size:12px;padding:5px 12px;text-transform:uppercase;letter-spacing:.3px}
  .option-title{position:absolute;color:var(--bright);font-weight:800;font-size:20px;line-height:1.1}
  .copy{position:absolute;font-size:10px;line-height:1.4;color:var(--ink);text-align:justify}
  .visual{position:absolute;border-radius:4px}
  .visual-xray{background:linear-gradient(135deg,#5b6d80,#b7c4d2 55%,#3e4d5e)}
  .visual-teeth{background:radial-gradient(ellipse at 50% 35%,#f7f7f7 0 35%,#efc2c7 60%,var(--gum) 100%)}
  .connector{position:absolute}
</style>
</head>
<body>
<main class="flyer">
  <svg class="header-shape" viewBox="0 0 600 300" aria-hidden="true">
    <path d="M0 0H600V230Q300 310 0 230Z" fill="var(--navy)"/>
    <path d="M8 240Q300 320 592 240" fill="none" stroke="var(--blue)" stroke-width="6"/>
  </svg>
  <h1 class="title">Single Missing Tooth</h1>
  <div class="subtitle-band">Your Options for Treatment</div>
  <p class="intro">A missing tooth is a serious issue. It can cause long-term damage to facial structure, bone density and your ability to feel confident in your smile.</p>
  <p class="pitch">Brightway Dental Studio has several options available to fix your missing tooth.</p>

  <div class="option-tag" style="left:200px;top:298px">Option 1:</div>
  <h2 class="option-title" style="left:292px;top:296px">Do Nothing</h2>
  <p class="copy" style="left:200px;right:30px;top:324px">If you choose to do nothing at this time, the cost down the road can be substantial. $20,000+ for orthodontics to straighten out the teeth, implant, abutment and crown, bone grafting and possible sinus lift to replace lost bone.</p>

  <div class="visual visual-xray" role="img" aria-label="Dental X-ray showing the gap of a missing tooth" style="left:24px;top:374px;width:200px;height:80px"></div>

  <div class="option-tag" style="left:240px;top:392px">Option 2:</div>
  <svg class="connector" style="left:330px;top:384px" width="60" height="30" aria-hidden="true"><path d="M2 16Q30 4 52 18" fill="none" stroke="var(--blue)" stroke-width="2"/><path d="M46 12L54 20L44 22" fill="none" stroke="var(--blue)" stroke-width="2"/></svg>
  <div class="visual visual-teeth" role="img" aria-label="Illustration of a dental implant with post, abutment and crown" style="left:390px;top:372px;width:190px;height:82px"></div>
  <h2 class="option-title" style="left:90px;top:460px">Dental Implant</h2>
  <p class="copy" style="left:24px;right:30px;top:486px">The bad news is that a dental implant is the most expensive option. BUT the good news is it is the most effective, functional and aesthetically pleasing. A dental implant will keep the bone in that area of the jaw from atrophy. It helps maintain face shape and prevents sunken face. The implant will prevent surrounding teeth from shifting and chances of losing the tooth decline. It will keep the teeth from shifting, and will prevent any future need to cut down the adjacent teeth. A dental implant is the nearest thing to a natural tooth available today.</p>

  <div class="option-tag" style="left:240px;top:568px">Option 3:</div>
  <h2 class="option-title" style="left:332px;top:566px">Dental Bridge</h2>
  <p class="copy" style="left:240px;right:24px;top:594px">The good news here is that a bridge is less expensive than the implant option BUT you will continue to lose bone in that area over time. Food will get caught in the hard to reach areas and if not cleaned properly could mean you have to replace the bridge every 7 years. In addition, to secure the bridge, the adjacent teeth must be cut down in order to be used as anchors for the appliance. Why cut down two good teeth if we don't have to?</p>
  <div class="visual visual-teeth" role="img" aria-label="Illustration of a three-unit dental bridge over prepared teeth" style="left:24px;top:586px;width:196px;height:96px"></div>

  <div class="option-tag" style="left:250px;top:704px">Option 4:</div>
  <h2 class="option-title" style="left:24px;top:702px;width:220px">The Removable Partial Denture (RPD)</h2>
  <p class="copy" style="left:24px;width:366px;top:752px">The good news here is that it's the least expensive option of the 4, but the BAD news is that your teeth have to come out every night. You won't be able to chew your food as well and your tongue will be uncomfortable with the big, bulky plastic sitting in your mouth all day.</p>
  <div class="visual visual-teeth" role="img" aria-label="Illustration of a removable partial denture replacing one tooth" style="left:404px;top:718px;width:176px;height:90px"></div>
</main>
</body>
</html>
```